LETTERHEAD & ENVELOPE: eye-catching stationary design for our custom office furniture business

Our company recently rebranded and we are in need of new stationary. Specifically, we need branded letterhead for standard paper size (8.5” x 11”), and matching envelopes, size: #9.

All designs should incorporate our brand colors, brand typeface, and logo. Please view attached brand guidelines document for brand colors, and brand description.

Letterhead: 8.5” x 11” Must include CedarlineKTV Logo, Talbot Greaves Certified Dealer Logo, mailing address, phone number, website, and email address.

Envelope: 9.5” x 4.125” Must include CedarlineKTV Logo, mailing address, and Talbot Greaves Certified Dealer Logo.

Attached files include:

```html
<!DOCTYPE html>
<html lang="en">
<head>
<meta charset="utf-8">
<title>CedarlineKTV Stationery</title>
<link href="https://fonts.googleapis.com/css2?family=Raleway:wght@300;400&family=Arimo:wght@400;700&display=swap" rel="stylesheet">
<style>
:root{
  --board:#d3d6d5;
  --paper:#ffffff;
  --brand:#5b7f71;
  --brand-tint:#e3e8e6;
  --brand-soft:#6f8c80;
  --ink:#111111;
}
*{margin:0;padding:0;box-sizing:border-box}
html,body{width:1200px;height:816px;overflow:hidden}
body{background:var(--board);position:relative;font-family:"Arimo",Arial,sans-serif;color:var(--ink)}
.sheet{position:absolute;overflow:hidden}
.letterhead{left:60px;top:70px;width:522px;height:671px;background:var(--paper)}
.envelope-back{left:633px;top:145px;width:510px;height:220px;background:var(--brand)}
.envelope-front{left:633px;top:447px;width:510px;height:221px;background:var(--paper)}
.backdrop{position:absolute;inset:0}
.brand{position:absolute;display:flex;align-items:center;gap:12px}
.brand-dot{border-radius:50%;background:var(--brand);flex:none}
.brand-name{font-family:"Raleway",sans-serif;font-weight:300;color:var(--brand);white-space:nowrap}
.contact{position:absolute;text-align:right;font-size:8.6px;line-height:9.4px;color:var(--ink)}
.dealer{position:absolute;display:flex;align-items:center;gap:9px}
.dealer-dot{border-radius:50%;flex:none}
.dealer-name{font-family:"Arimo",sans-serif;white-space:nowrap;letter-spacing:-0.2px}
.salutation,.date{position:absolute;top:198px;font-size:12px}
.salutation{left:44px}
.date{right:35px}
.letter-body{position:absolute;left:73px;top:251px;width:370px;font-size:8.2px;line-height:15.5px;font-weight:700;text-align:justify}
</style>
</head>
<body>

<section class="sheet letterhead">
  <svg class="backdrop" width="522" height="671" aria-hidden="true">
    <circle cx="190" cy="340" r="150" fill="var(--brand-tint)"/>
  </svg>
  <div class="brand" style="left:44px;top:49px">
    <span class="brand-dot" style="width:40px;height:40px"></span>
    <span class="brand-name" style="font-size:27px">CedarlineKTV</span>
  </div>
  <address class="contact" style="right:35px;top:33px;font-style:normal">
    418 NW Alder Row, Suite 310<br>Rivermont, OR 97410<br>555.014.2290<br>info@cedarlinektv.com<br>www.cedarlinektv.com
  </address>
  <p class="salutation">Dear Dana Whitfield,</p>
  <p class="date">Aug 10 / 2021</p>
  <div class="letter-body">
    <p>Lorem ipsum dolor sit amet, consectetuer adipiscing elit, sed diam nonummy nibh euismod tincidunt ut laoreet dolore magna aliquam erat volutpat. Ut wisi enim ad minim veniam, quis nostrud exerci tation ullamcorper suscipit lobortis nisl ut aliquip ex ea commodo consequat. Duis autem vel eum iriure dolor in hendrerit in vulputate velit esse molestie consequat, vel illum dolore eu feugiat nulla facilisis at vero eros et accumsan et iusto odio dignissim qui blandit praesent luptatum zzril delenit augue duis dolore te feugait nulla facilisi.</p>
    <p>Lorem ipsum dolor sit amet, cons ectetuer adipiscing elit, sed diam nonummy nibh euismod tincidunt ut laoreet dolore magna aliquam erat volutpat. Ut wisi enim ad minim veniam, quis nostrud exerci tation ullam</p>
  </div>
  <div class="dealer" style="left:44px;top:613px">
    <span class="dealer-dot" style="width:28px;height:28px;background:var(--ink)"></span>
    <span class="dealer-name" style="font-size:13px;color:var(--ink)">Talbot Greaves Certified Dealer</span>
  </div>
</section>

<section class="sheet envelope-back">
  <svg class="backdrop" width="510" height="220" aria-hidden="true">
    <circle cx="120" cy="110" r="95" fill="none" stroke="var(--brand-soft)" stroke-width="42"/>
  </svg>
  <div class="dealer" style="left:38px;top:107px">
    <span class="dealer-dot" style="width:36px;height:36px;background:var(--paper)"></span>
    <span class="dealer-name" style="font-size:16px;color:var(--paper)">Talbot Greaves Certified Dealer</span>
  </div>
</section>

<section class="sheet envelope-front">
  <svg class="backdrop" width="510" height="221" aria-hidden="true">
    <circle cx="120" cy="150" r="110" fill="var(--brand-tint)"/>
    <polygon points="0,0 510,0 490,67 20,67" fill="var(--brand)"/>
  </svg>
  <div class="brand" style="left:24px;top:161px">
    <span class="brand-dot" style="width:40px;height:40px"></span>
    <span class="brand-name" style="font-size:29px">CedarlineKTV</span>
  </div>
  <address class="contact" style="right:23px;top:146px;font-style:normal;line-height:10.5px">
    418 NW Alder Row, Suite 310<br>Rivermont, OR 97410<br>555.014.2290<br>info@cedarlinektv.com<br>www.cedarlinektv.com
  </address>
</section>

</body>
</html>
```